An anniversary gift for my girlfriend

My girlfriend and I have been dating for almost 2 years. We met online and this has afforded us the really unique opportunity to have the first words we said to each other (the whole conversation, in fact) preserved. We're moving in together in a few months and she doesn't know that I saved the conversation. I've been waiting for this to turn it into something we can hang in our new place.

The only phrase I want to use is:
"Well if you dislike people's knees then I think we'll get along famously"

It's an Nobody Leaves Before Midnight in Portland reference for the curious.

I want the poster to use the words themselves as the art; I'm thinking typography. I'd like it to match her aesthetic, she likes to wear Nora Vell and T. Brisk. Colors shouldn't be anything too "girly". Somewhere I'd like to include the date June 1, 2015. It shouldn't be a major piece of the poster though, just a way to denote the date.

It should fit (and be fully visible in) a 16x20 (inches) frame

Thanks in advance for the work!

Requirements
Must have
• Must use only the words: "Well if you dislike people's knees then I think we'll get along famously"
• I want this to be typography, so making the phrase the center of the poster and the art itself.

```html
<!DOCTYPE html>
<html lang="en">
<head>
<meta charset="utf-8">
<title>Well If You Dislike People's Knees — Anniversary Poster</title>
<link rel="stylesheet" href="https://fonts.googleapis.com/css2?family=Montserrat:wght@500;600;900&family=Playfair+Display:wght@400&family=Raleway:wght@200&display=swap">
<style>
  :root {
    --sky-top: #ebe7e2;
    --sky-bottom: #c8bcb1;
    --sun-top: #e2bcaa;
    --sun-bottom: #c9a08e;
    --ink: #0a0a0a;
    --date: #ffffff;
    --flake: rgba(255, 255, 255, 0.55);
    --village-top: rgba(196, 176, 164, 0);
    --village-mid: #b49c8e;
    --village-bottom: #9c8174;
    --snow: #ffffff;
  }
  html, body {
    margin: 0;
    padding: 0;
    overflow: hidden;
    background: var(--sky-bottom);
  }
  .poster {
    position: relative;
    width: 960px;
    height: 1200px;
    overflow: hidden;
    background: linear-gradient(180deg, var(--sky-top) 0%, var(--sky-bottom) 100%);
  }
  .snowfall {
    position: absolute;
    inset: 0;
    background-image:
      radial-gradient(circle, var(--flake) 0 3px, transparent 3.5px),
      radial-gradient(circle, var(--flake) 0 2px, transparent 2.5px),
      radial-gradient(circle, var(--flake) 0 4px, transparent 4.5px),
      radial-gradient(circle, var(--flake) 0 1.5px, transparent 2px);
    background-size: 137px 131px, 89px 97px, 211px 193px, 53px 61px;
    background-position: 11px 23px, 47px 5px, 120px 80px, 30px 40px;
    opacity: 0.8;
  }
  .sun {
    position: absolute;
    left: 60px;
    top: 54px;
    width: 840px;
    height: 840px;
    border-radius: 50%;
    background: linear-gradient(180deg, var(--sun-top), var(--sun-bottom));
  }
  .quote {
    position: absolute;
    left: 0;
    top: 0;
    width: 960px;
    height: 900px;
  }
  .quote text { fill: var(--ink); }
  .serif { font-family: "Playfair Display", serif; font-weight: 400; }
  .sans-heavy { font-family: "Montserrat", sans-serif; font-weight: 900; }
  .sans-thin { font-family: "Raleway", sans-serif; font-weight: 200; }
  .sans-medium { font-family: "Montserrat", sans-serif; font-weight: 500; }
  .quote .outline { fill: none; stroke: var(--ink); stroke-width: 1.2; }
  .date {
    position: absolute;
    left: 0;
    top: 822px;
    width: 960px;
    margin: 0;
    text-align: center;
    font-family: "Montserrat", sans-serif;
    font-weight: 600;
    font-size: 34px;
    color: var(--date);
    letter-spacing: 1px;
  }
  .village {
    position: absolute;
    left: 0;
    top: 900px;
    width: 960px;
    height: 300px;
  }
</style>
</head>
<body>
  <main class="poster">
    <div class="snowfall" aria-hidden="true"></div>
    <div class="sun"></div>

    <svg class="quote" viewBox="0 0 960 900" aria-label="Well if you dislike people's knees then I think we'll get along famously">
      <text class="serif" x="78" y="234" font-size="165" textLength="516" lengthAdjust="spacingAndGlyphs">WELL</text>
      <text class="sans-thin" x="606" y="180" font-size="56" textLength="276" lengthAdjust="spacingAndGlyphs">IF YOU</text>
      <text class="sans-heavy" x="606" y="234" font-size="58" textLength="276" lengthAdjust="spacingAndGlyphs">DISLIKE</text>
      <text class="sans-heavy" x="78" y="342" font-size="100" textLength="804" lengthAdjust="spacingAndGlyphs">PEOPLE'S KNEES</text>
      <text class="serif" x="78" y="498" font-size="190" textLength="486" lengthAdjust="spacingAndGlyphs">THEN</text>
      <text class="sans-heavy" x="576" y="432" font-size="62" textLength="306" lengthAdjust="spacingAndGlyphs">I THINK</text>
      <text class="sans-thin outline" x="576" y="494" font-size="64" textLength="306" lengthAdjust="spacingAndGlyphs">WE'LL</text>
      <text class="sans-heavy" x="78" y="636" font-size="150" textLength="804" lengthAdjust="spacingAndGlyphs">GET ALONG</text>
      <text class="sans-medium" x="78" y="786" font-size="160" textLength="804" lengthAdjust="spacingAndGlyphs">FAMOUSLY</text>
    </svg>

    <p class="date">JUNE 1, 2015</p>

    <svg class="village" viewBox="0 0 960 300">
      <defs>
        <linearGradient id="village-tone" x1="0" y1="0" x2="0" y2="1">
          <stop offset="0" stop-color="var(--village-top)"/>
          <stop offset="0.45" stop-color="var(--village-mid)" stop-opacity="0.55"/>
          <stop offset="1" stop-color="var(--village-bottom)" stop-opacity="0.85"/>
        </linearGradient>
      </defs>
      <rect x="0" y="40" width="960" height="150" fill="url(#village-tone)" role="img" aria-label="Illustration of a snow-covered village of small houses with a red church steeple"/>
      <path d="M0 160 C90 150 170 170 260 162 C360 152 420 178 520 176 C610 174 650 158 740 160 C830 162 900 150 960 152 L960 300 L0 300 Z" fill="var(--snow)"/>
    </svg>
  </main>
</body>
</html>
```